The Perfect Business Card for PineHarbor

I am looking for a business card which beautifully incorporates my logo, reflects my business and looks special, elegant and clean.

```html
<!DOCTYPE html>
<html lang="en">
<head>
<meta charset="utf-8">
<title>PineHarbor Business Card</title>
<link rel="stylesheet" href="https://fonts.googleapis.com/css2?family=Cinzel:wght@400;600&family=Open+Sans:wght@400&display=swap">
<style>
  :root {
    --page: #d9dadc;
    --green-dark: #4e6a2b;
    --green-mid: #5a7634;
    --green-light: #648038;
    --green-emboss: #4a6427;
    --green-text: #5f8a2e;
    --green-ink: #3f5a1f;
    --white: #ffffff;
  }
  * { margin: 0; padding: 0; box-sizing: border-box; }
  html, body { width: 900px; height: 1200px; overflow: hidden; }
  body { background: var(--page); position: relative; font-family: "Open Sans", sans-serif; }

  .card {
    position: absolute;
    left: 169px;
    width: 562px;
    height: 362px;
    border-radius: 24px;
    overflow: hidden;
  }
  .card-front {
    top: 202px;
    background: linear-gradient(160deg, var(--green-dark) 0%, var(--green-mid) 50%, var(--green-light) 100%);
  }
  .card-back { top: 635px; background: var(--white); }

  .brand { position: absolute; display: flex; align-items: center; }
  .brand-dot { border-radius: 50%; flex: none; }
  .brand-name { font-family: "Cinzel", serif; font-weight: 400; line-height: 1; }

  .card-front .brand { left: 84px; top: 160px; }
  .card-front .brand-dot { width: 30px; height: 30px; background: var(--green-emboss); margin-right: 18px; }
  .card-front .brand-name { font-size: 44px; color: var(--green-emboss); }

  .card-back .brand { left: 36px; top: 72px; }
  .card-back .brand-dot { width: 22px; height: 22px; background: var(--green-text); margin-right: 13px; }
  .card-back .brand-name { font-size: 33px; color: var(--green-text); }

  .contact {
    position: absolute;
    left: 384px;
    top: 34px;
    list-style: none;
    color: var(--green-ink);
    font-size: 14px;
    letter-spacing: 0.3px;
  }
  .contact li { display: flex; align-items: center; height: 22.5px; }
  .contact svg { width: 11px; height: 11px; margin-right: 3px; fill: var(--green-text); }
  .contact .address { height: auto; line-height: 24px; margin-top: 4px; display: block; }

  .person-name {
    position: absolute;
    left: 36px;
    top: 200px;
    font-family: "Cinzel", serif;
    font-weight: 600;
    font-size: 22px;
    letter-spacing: 1px;
    color: var(--green-ink);
  }
  .credentials {
    position: absolute;
    left: 36px;
    top: 239px;
    font-size: 13.5px;
    line-height: 19px;
    color: var(--green-text);
  }
</style>
</head>
<body>
  <section class="card card-front" aria-label="Card front">
    <div class="brand">
      <span class="brand-dot"></span>
      <span class="brand-name">PineHarbor</span>
    </div>
  </section>

  <section class="card card-back" aria-label="Card back">
    <div class="brand">
      <span class="brand-dot"></span>
      <span class="brand-name">PineHarbor</span>
    </div>

    <ul class="contact">
      <li>
        <svg viewBox="0 0 24 24" aria-hidden="true"><path d="M6.6 10.8a15.1 15.1 0 0 0 6.6 6.6l2.2-2.2c.3-.3.7-.4 1-.2 1.1.4 2.3.6 3.6.6.6 0 1 .4 1 1V20c0 .6-.4 1-1 1A17 17 0 0 1 3 4c0-.6.4-1 1-1h3.5c.6 0 1 .4 1 1 0 1.3.2 2.5.6 3.6.1.3 0 .7-.2 1z"/></svg>
        +41 (0)70 555 28 40
      </li>
      <li>
        <svg viewBox="0 0 24 24" aria-hidden="true"><path d="M2 5h20L12 13z"/><path d="M2 7l10 8 10-8v12H2z"/></svg>
        info@pineharbor.ch
      </li>
      <li>
        <svg viewBox="0 0 24 24" aria-hidden="true"><circle cx="12" cy="12" r="10" fill="none" stroke="#5f8a2e" stroke-width="2"/><ellipse cx="12" cy="12" rx="4" ry="10" fill="none" stroke="#5f8a2e" stroke-width="2"/><path d="M2 12h20" stroke="#5f8a2e" stroke-width="2"/></svg>
        www.pineharbor.ch
      </li>
      <li class="address">Birkenweg 7,<br>8003 Zürich</li>
    </ul>

    <h1 class="person-name">Dr. Mara Eldwin</h1>
    <p class="credentials">
      Organizational &amp; Health Psychologist,<br>
      Licensed Naturopath (Classical European Naturopathic Medicine),<br>
      Certified Life Coach, Ayurvedic Consultant,<br>
      Certified Clinical Hypnotherapist,<br>
      Yoga &amp; Breathwork Therapist.
    </p>
  </section>
</body>
</html>
```